One page flyer for nonprofit focused IT company

I need a one page flyer (one side of a single 8.5x11 page) with text and graphics. The company logo is already done, and it must appear on the flyer along with other icons and graphics. The final design will be printed on heavy weight glossy paper as a handout and also distributed as a PDF.

The text is provided in an attachment, if it needs to be shortened let me know.

Industry/Entity Type

Information Technology

Requirements
Must have
• some flare (colors, icons or images)
Should not have
• While we work for nonprofits, my company is a FOR PROFIT company.

```html
<!DOCTYPE html>
<html lang="en">
<head>
<meta charset="utf-8">
<title>Meridian Systems Group – Nonprofit IT Services Flyer</title>
<link href="https://fonts.googleapis.com/css2?family=Montserrat:wght@600;700;800&family=Arimo:wght@400&display=swap" rel="stylesheet">
<style>
  :root {
    --wine: #93132a;
    --charcoal: #4a4a4a;
    --page: #ffffff;
    --backdrop: #262626;
    --ink: #1e1e1e;
    --heading-font: "Montserrat", sans-serif;
    --body-font: "Arimo", Arial, sans-serif;
  }
  * { margin: 0; padding: 0; box-sizing: border-box; }
  html, body { width: 945px; height: 1200px; overflow: hidden; background: var(--backdrop); }
  .flyer {
    position: absolute; left: 9px; top: 0; width: 927px; height: 1200px;
    background: var(--page); overflow: hidden; color: var(--ink);
  }
  .abs { position: absolute; }

  /* Brand */
  .brand-name {
    left: 30px; width: 340px; top: 74px; text-align: center;
    font-family: var(--heading-font); font-weight: 700; font-size: 27px; line-height: 1;
    color: var(--wine); letter-spacing: 0.3px;
  }

  /* Title banner */
  .title-band { left: 444px; top: 27px; width: 483px; height: 168px; }
  .title-text {
    right: 42px; top: 50px; text-align: right; color: #fff;
    font-family: var(--heading-font); font-weight: 800; line-height: 1;
  }
  .title-text .small { font-size: 34px; display: block; margin-bottom: 3px; }
  .title-text .large { font-size: 46px; display: block; margin-top: 2px; }

  /* Hero */
  .hero-photo {
    left: 344px; top: 213px; width: 583px; height: 368px;
    background:
      radial-gradient(circle at 66% 48%, rgba(255,230,190,0.95) 0, rgba(140,190,240,0.6) 6%, rgba(40,90,170,0.3) 24%, transparent 45%),
      linear-gradient(120deg, #0c2248 0%, #1d4b8a 45%, #0d2350 80%, #071530 100%);
  }
  .hero-panel { left: 0; top: 178px; width: 570px; height: 404px; }
  .hero-heading {
    left: 46px; top: 218px; width: 260px; color: #fff;
    font-family: var(--heading-font); font-weight: 800; font-size: 24px; line-height: 32px;
  }
  .hero-copy {
    left: 46px; top: 364px; width: 400px; color: #fff;
    font-family: var(--body-font); font-size: 15.4px; line-height: 22.8px;
  }
  .hero-copy .line { display: block; white-space: nowrap; }

  /* Section tags */
  .section-tag { height: 38px; }
  .section-tag svg { position: absolute; left: 0; top: 0; }
  .section-tag span {
    position: absolute; left: 17px; top: 5px; color: #fff;
    font-family: var(--heading-font); font-weight: 800; font-size: 23px; letter-spacing: 0.3px;
  }
  .tag-successes { left: 54px; top: 607px; width: 232px; }
  .tag-solutions { left: 464px; top: 607px; width: 232px; }

  /* Items */
  .item-title {
    font-family: var(--heading-font); font-weight: 700; font-size: 15.5px;
    color: var(--wine); line-height: 17.5px;
  }
  .item-copy {
    font-family: var(--body-font); font-size: 12.6px; line-height: 17.5px; color: var(--ink);
  }
  .success { left: 51px; width: 362px; }
  .solution { left: 524px; width: 356px; }
  .solution-icon { left: 460px; width: 55px; height: 55px; }

  /* Footer */
  .footer-shapes { left: 0; top: 1127px; width: 927px; height: 73px; }
  .footer-web {
    left: 61px; top: 1152px; display: flex; align-items: center; gap: 10px;
    font-family: var(--heading-font); font-weight: 800; font-size: 17.5px; color: #fff;
  }
  .footer-contact {
    left: 500px; top: 1171px; display: flex; align-items: center; gap: 8px;
    font-family: var(--heading-font); font-weight: 600; font-size: 14px; color: #fff;
  }
  .footer-contact .gap { width: 6px; }
</style>
</head>
<body>
<main class="flyer">

  <div class="abs brand-name">Meridian Systems Group</div>

  <svg class="abs title-band" viewBox="0 0 483 168" aria-hidden="true">
    <polygon points="0,168 97,0 105,0 8,168" fill="var(--charcoal)"/>
    <polygon points="14,168 111,0 119,0 22,168" fill="var(--charcoal)"/>
    <polygon points="30,168 127,0 483,0 483,168" fill="var(--charcoal)"/>
  </svg>
  <h1 class="abs title-text">
    <span class="small">50 YEARS</span>
    <span class="small">OF NONPROFIT</span>
    <span class="large">IT SERVICES</span>
  </h1>

  <div class="abs hero-photo" role="img" aria-label="Photo of a businessman's hand touching a glowing holographic technology interface on a deep blue background"></div>
  <svg class="abs hero-panel" viewBox="0 0 570 404" aria-hidden="true">
    <polygon points="0,0 344,0 568,404 0,404" fill="var(--wine)"/>
  </svg>
  <h2 class="abs hero-heading">An Efficient and Elegant Approach to IT Solution Implementations</h2>
  <p class="abs hero-copy">
    <span class="line">Meridian Systems Group has been</span>
    <span class="line">supporting the Information Systems needs of</span>
    <span class="line">nonprofits for over 50 years.&nbsp; We continually strive</span>
    <span class="line">to bring the latest technologies and best practices</span>
    <span class="line">to nonprofits to drive down the cost of IT while</span>
    <span class="line">implementing systems that drive revenue.&nbsp; Our Agile</span>
    <span class="line">approach to IT management means that we deliver working</span>
    <span class="line">systems to every one of our clients every two weeks.</span>
  </p>

  <div class="abs section-tag tag-successes">
    <svg width="232" height="38" viewBox="0 0 232 38" aria-hidden="true">
      <rect x="0" y="0" width="186" height="38" fill="var(--wine)"/>
      <polygon points="188,0 195,0 216,38 209,38" fill="var(--wine)"/>
      <polygon points="200,0 208,0 232,38 224,38" fill="var(--wine)"/>
    </svg>
    <span>SUCCESSES</span>
  </div>
  <div class="abs section-tag tag-solutions">
    <svg width="232" height="38" viewBox="0 0 232 38" aria-hidden="true">
      <rect x="0" y="0" width="186" height="38" fill="var(--wine)"/>
      <polygon points="188,0 195,0 216,38 209,38" fill="var(--wine)"/>
      <polygon points="200,0 208,0 232,38 224,38" fill="var(--wine)"/>
    </svg>
    <span>SOLUTIONS</span>
  </div>

  <section class="abs success" style="top:673px">
    <h3 class="item-title">90% Reduction in Software Development Costs</h3>
    <p class="item-copy">Harlow's National Auto Retailers Guild needed to update their core product offering; they engaged their in-house IT department who estimated the project would take 3 years at a cost of $3,000,000.&nbsp; NARG decided to work with Meridian Systems Group instead, and the product was released to production in only 9 months at one tenth of the cost, only $300,000</p>
  </section>
  <section class="abs success" style="top:848px">
    <h3 class="item-title">10x Increase in Membership</h3>
    <p class="item-copy">Greenway Paths Trust needed to move to online membership registration and contracted with Meridian Systems Group to build a significant online presence and engage potential members.&nbsp; Through compelling online tools and mobile applications Greenway Paths has increased membership 10 fold.</p>
  </section>
  <section class="abs success" style="top:969px">
    <h3 class="item-title">20% Reduction in Overhead</h3>
    <p class="item-copy">The National Alliance for Civic Voices had antiquated systems and processes in place to manage over 500 chapters across the nation.&nbsp; Working with MSG they implemented online tools to allow communication and management between the local chapters and national headquarters.&nbsp; This eliminated much of the overhead of chapter management, reducing HR costs by 20%.</p>
  </section>

  <svg class="abs solution-icon" style="top:661px" viewBox="0 0 55 55" aria-hidden="true">
    <circle cx="27.5" cy="27.5" r="27.5" fill="var(--wine)"/>
    <g fill="none" stroke="#fff" stroke-width="1.6">
      <rect x="14" y="16" width="22" height="16" rx="1.5"/><path d="M21 38h8M25 32v6"/>
      <rect x="31" y="21" width="10" height="17" rx="1.5"/>
    </g>
  </svg>
  <svg class="abs solution-icon" style="top:749px" viewBox="0 0 55 55" aria-hidden="true">
    <circle cx="27.5" cy="27.5" r="27.5" fill="var(--wine)"/>
    <g fill="none" stroke="#fff" stroke-width="1.6">
      <rect x="18" y="12" width="17" height="31" rx="2"/><path d="M18 17h17M18 38h17M38 24h6M38 28h6M38 32h4"/>
      <circle cx="26.5" cy="27.5" r="4.5"/>
    </g>
  </svg>
  <svg class="abs solution-icon" style="top:838px" viewBox="0 0 55 55" aria-hidden="true">
    <circle cx="27.5" cy="27.5" r="27.5" fill="var(--wine)"/>
    <g fill="none" stroke="#fff" stroke-width="1.6">
      <circle cx="24" cy="27.5" r="8"/><circle cx="24" cy="27.5" r="3"/>
      <path d="M32 22h6l3-4M32 33h6l3 4M32 27.5h10"/>
    </g>
  </svg>
  <svg class="abs solution-icon" style="top:919px" viewBox="0 0 55 55" aria-hidden="true">
    <circle cx="27.5" cy="27.5" r="27.5" fill="var(--wine)"/>
    <g fill="none" stroke="#fff" stroke-width="1.6">
      <rect x="14" y="30" width="5" height="10"/><rect x="22" y="22" width="5" height="18"/>
      <rect x="30" y="26" width="5" height="14"/><rect x="38" y="16" width="5" height="24"/>
    </g>
  </svg>
  <svg class="abs solution-icon" style="top:986px" viewBox="0 0 55 55" aria-hidden="true">
    <circle cx="27.5" cy="27.5" r="27.5" fill="var(--wine)"/>
    <path d="M17 35a7 7 0 0 1 1-14 10 10 0 0 1 19-2 8 8 0 0 1 1 16z" fill="none" stroke="#fff" stroke-width="1.6"/>
  </svg>
  <svg class="abs solution-icon" style="top:1047px" viewBox="0 0 55 55" aria-hidden="true">
    <circle cx="27.5" cy="27.5" r="27.5" fill="var(--wine)"/>
    <g fill="none" stroke="#fff" stroke-width="1.6">
      <ellipse cx="27.5" cy="17" rx="10" ry="3.5"/>
      <path d="M17.5 17v20c0 2 4.5 3.5 10 3.5s10-1.5 10-3.5V17M17.5 27c0 2 4.5 3.5 10 3.5s10-1.5 10-3.5"/>
    </g>
  </svg>

  <section class="abs solution" style="top:664px">
    <h3 class="item-title">Web Applications</h3>
    <p class="item-copy">With a focus on non-profit websites and web based applications, MSG helps nonprofits communicate with their members and donors while maximizing online giving and engagement.</p>
  </section>
  <section class="abs solution" style="top:751px">
    <h3 class="item-title">Mobile Applications</h3>
    <p class="item-copy">Meridian Systems Group implements mobile applications for phones and tablets to provide direct communications with members and donors enabling real-time, two way interaction.</p>
  </section>
  <section class="abs solution" style="top:838px">
    <h3 class="item-title">Systems Integration</h3>
    <p class="item-copy">Every nonprofit's IT applications are scattered and disconnected.&nbsp; Meridian Systems Group has decades of experience integrating these applications into a single cohesive system.</p>
  </section>
  <section class="abs solution" style="top:924px">
    <h3 class="item-title">Business Intelligence and Reporting</h3>
    <p class="item-copy">Meridian Systems Group can wrestle all of an organization's data into simple executive dashboards and reports.</p>
  </section>
  <section class="abs solution" style="top:995px">
    <h3 class="item-title">Cloud Migration</h3>
    <p class="item-copy">Reduce IT costs by migrating to the latest cloud solutions.</p>
  </section>
  <section class="abs solution" style="top:1047px">
    <h3 class="item-title">Member Donor Database</h3>
    <p class="item-copy">Meridian Systems Group's GiveLedger Member / Donor CRM system is fully customized for each client meeting the unique needs of your organization.</p>
  </section>

  <svg class="abs footer-shapes" viewBox="0 0 927 73" aria-hidden="true">
    <polygon points="0,0 415,0 455,73 0,73" fill="var(--wine)"/>
    <polygon points="447,28 927,28 927,73 467,73" fill="var(--charcoal)"/>
  </svg>
  <div class="abs footer-web">
    <svg width="26" height="26" viewBox="0 0 26 26" aria-hidden="true">
      <g fill="none" stroke="#fff" stroke-width="2">
        <circle cx="13" cy="13" r="11"/><ellipse cx="13" cy="13" rx="5" ry="11"/><path d="M2 13h22"/>
      </g>
    </svg>
    <span>www.meridiansysgroup.com</span>
  </div>
  <div class="abs footer-contact">
    <svg width="20" height="20" viewBox="0 0 20 20" aria-hidden="true">
      <path d="M4 2l3 4-2 2a11 11 0 0 0 6 6l2-2 4 3-2 3C8 18 2 12 1 4z" fill="none" stroke="#fff" stroke-width="1.6"/>
    </svg>
    <span>010 48 20 71 39</span>
    <span class="gap"></span>
    <svg width="18" height="14" viewBox="0 0 18 14" aria-hidden="true">
      <rect x="1" y="1" width="16" height="12" fill="none" stroke="#fff" stroke-width="1.6"/>
      <path d="M1 1l8 7 8-7" fill="none" stroke="#fff" stroke-width="1.6"/>
    </svg>
    <span>mail@meridiansysgroup.com</span>
  </div>

</main>
</body>
</html>
```